Design clean technology service-based company website

Hello, We are looking to reskin our company website. We are an environmental inspection company and test for Asbestos, Lead and Mold along with other contaminants. People depend on the results to be accurate and fast. We are regulated by the EPA and State regulations. We work a lot with business to business and business to customer. We are wanting to make our new presentation to be modern and easy for customers to interact with us, understand our process and services while providing valuable environmental informational resource and updates. We are a technology based company and will be providing instantaneous results as reports come in for the customers. We are needing good calls to action on the site to direct them to setup a new inspection. Each user will have a backend access to their job information with invoices, reports, status, etc. We have developed software to be able to proved these reports and want to look the part.

My current website is www.trypelmarix.com

Helllo we are wanting to make sure we have good time to select the right website for us and also have the additional time to select other pages of the website. We have received great designs and have consolidated our requests into a document for the next set of iterations.

Target Market(s)

Home Owners, Contractors, Engineers, Real Estate Agents, Building Owners, Insurance Adjusters

Industry/Entity Type

Environmental Consultant

Number of Pages Required

5+ page

Font styles to use
Sans Serif

Colors
0355a3
9bcb3c
7f7f7f
f5f5f5
000000

Requirements
Must have
• Use our existing logo to design around
• The layouts look good in mobile mode for understanding and selecting services and signing up
• Clean Modern Layout
• Have all pages on the website have a similar layout and feel
• Clearly communicate services along with bundle service packages
• Detail the customer journey with graphic design
• Great call to actions to either schedule inspection online, call, text, chat
Nice to have
• Have an interactive graphic for where to test for lead, asbestos and mold.
• I like the barney kolts top order line bar - see attached
• Have clear question and answer page layouts for asbestos, lead and mold
• Show Company reviews
• Have clear Resources pages for all types of contaminants
Should not have
• My current website is www.trypelmarix.com

```html
<!DOCTYPE html>
<html lang="en">
<head>
<meta charset="utf-8">
<title>Trypelmarix – Asbestos, Mold, Lead Inspections</title>
<link href="https://fonts.googleapis.com/css2?family=Roboto:wght@300;400;500;700;900&display=swap" rel="stylesheet">
<style>
:root{
  --blue:#0355a3;
  --blue-dark:#0a3f7a;
  --navy:#0c2c55;
  --green:#9bcb3c;
  --grey:#7f7f7f;
  --light:#f5f5f5;
  --ink:#000000;
  --footer:#3a3a3a;
  --footer-dark:#2b2b2b;
  --white:#ffffff;
}
*{box-sizing:border-box;margin:0;padding:0}
html,body{width:1200px;height:4489px;overflow:hidden}
body{font-family:"Roboto",Arial,sans-serif;color:#333;background:var(--white);position:relative}
.abs{position:absolute}
a{color:inherit;text-decoration:none}

/* top bar */
.topbar{left:0;top:0;width:1200px;height:30px;background:var(--blue-dark);color:#fff;font-size:11px;display:flex;align-items:center;padding:0 160px;justify-content:space-between}
.topbar span{margin-right:24px}

/* hero */
.hero{left:0;top:30px;width:1200px;height:870px;background:linear-gradient(160deg,#1d5fa8 0%,#0c4b93 45%,#0a3f82 100%)}
.hero-photo{left:0;top:0;width:1200px;height:870px;background:radial-gradient(ellipse at 60% 35%,rgba(180,205,235,.45),rgba(10,60,130,0) 60%)}
.header{left:160px;top:10px;width:880px;height:80px;background:#fff;display:flex;align-items:center;padding:0 18px;box-shadow:0 2px 6px rgba(0,0,0,.2)}
.brand{display:flex;align-items:center;gap:8px;font-weight:700;font-size:26px;color:var(--blue)}
.brand-dot{width:14px;height:14px;border-radius:50%;background:var(--green)}
.nav{margin-left:auto;display:flex;gap:16px;font-size:11px;color:#333;text-transform:uppercase}
.hero-text{left:160px;top:205px;color:#fff}
.hero-text .welcome{font-size:16px;font-weight:500;margin-bottom:8px}
.hero-text .welcome b{color:var(--green)}
.hero-text h1{font-size:36px;font-weight:900;line-height:40px}
.hero-text h1 .g{color:var(--green)}
.hero-text p{font-size:18px;margin-top:12px;line-height:22px;width:560px}
.btn-white{display:inline-block;margin-top:22px;background:#fff;color:var(--blue-dark);font-size:12px;font-weight:700;padding:12px 16px}
.signup-shadow{left:785px;top:465px;width:270px;height:395px;background:var(--green)}
.signup{left:763px;top:443px;width:270px;height:395px;background:#fff;padding:22px 26px;box-shadow:0 4px 12px rgba(0,0,0,.2)}
.signup h3{font-size:19px;font-weight:700;color:#333;line-height:22px;margin-bottom:20px;text-align:center}
.field{height:30px;background:#ececec;margin-bottom:12px;font-size:9px;color:#999;padding:9px 8px}
.field.tall{height:82px}
.btn-blue{display:inline-block;background:var(--blue);color:#fff;font-size:12px;font-weight:700;padding:9px 22px}

/* section heads */
.num{font-size:80px;font-weight:900;color:var(--green);line-height:70px}
.sec-title{font-size:28px;font-weight:700;color:#222}

/* why */
.why-photo{left:135px;top:895px;width:405px;height:545px;background:linear-gradient(180deg,#e7e7e7,#c9d3de 60%,#2d5ea6 60.5%,#204f94)}
.why-head{left:590px;top:935px;display:flex;align-items:flex-end;gap:6px}
.why-item{left:600px;width:480px}
.why-item h4{font-size:13px;font-weight:500;color:#222;margin-bottom:6px;display:flex;align-items:center;gap:10px}
.why-item p{font-size:11px;line-height:15px;color:#555;padding-left:30px}

/* construction band */
.band{left:0;top:1458px;width:1200px;height:150px;background:var(--green)}
.band-blue{left:0;top:1458px;width:440px;height:150px;background:var(--blue)}
.band-text{left:480px;top:1478px;width:560px}
.band-title{font-size:34px;font-weight:700;color:#222;line-height:40px}
.band-text p{font-size:11px;color:#fff;width:480px;line-height:15px;margin-top:6px}
.btn-navy{background:var(--navy);color:#fff;font-size:13px;font-weight:700;padding:12px 22px;display:inline-block}

/* services */
.svc-intro{left:480px;top:1685px;width:560px;font-size:11px;line-height:16px;color:#444}
.svc-label{width:300px;text-align:center;font-size:21px;font-weight:700;color:var(--blue)}

/* about */
.about{left:0;top:2200px;width:1200px;height:570px;background:linear-gradient(180deg,#ececec,#d8d8d8)}
.about-photo{left:225px;top:2345px;width:200px;height:240px;background:linear-gradient(180deg,#c8c8c8,#6f7c8a);border:3px solid #fff}
.about-name{left:225px;top:2595px}
.about-name h4{font-size:20px;color:var(--blue);font-weight:700}
.about-name span{font-size:11px;color:#444}
.about-bio{left:225px;top:2645px;width:380px;font-size:11px;line-height:15px;color:#444}
.about-copy{left:608px;top:2230px;width:440px}
.about-copy h3{font-size:22px;font-weight:700;color:var(--green);margin-bottom:8px}
.about-copy p{font-size:11px;line-height:15px;color:#444;margin-bottom:10px}

/* call band */
.callband{left:0;top:2770px;width:1200px;height:193px;background:var(--light)}
.callbtn{left:410px;top:2813px;width:377px;height:60px;background:var(--blue);color:#fff;font-size:24px;font-weight:700;display:flex;align-items:center;justify-content:center;gap:10px;box-shadow:0 3px 6px rgba(0,0,0,.25)}

/* blog */
.blog-blue{left:159px;top:2996px;width:275px;height:335px;background:var(--blue);color:#fff;padding:20px}
.blog-blue h3{font-size:26px;font-weight:700;margin-top:-6px}
.blog-blue p{font-size:11px;line-height:15px;margin-top:30px}
.card{background:#fff;box-shadow:0 3px 12px rgba(0,0,0,.18)}
.card .meta{font-size:11px;color:#333;font-weight:500}
.card h4{font-size:22px;line-height:26px;color:var(--blue);font-weight:700}
.card p{font-size:10px;line-height:14px;color:#555}

/* testimonial */
.testi{left:0;top:3436px;width:1200px;height:416px;background:linear-gradient(180deg,#1b5ba3,#0a3f82)}
.testi-avatar{left:535px;top:3445px;width:130px;height:130px;border-radius:50%;background:linear-gradient(180deg,#b9c4d0,#3c5675);border:4px solid #fff}
.testi-quote{left:220px;top:3665px;width:760px;text-align:center;color:#fff;font-size:16px;line-height:24px}
.testi-name{left:0;top:3755px;width:1200px;text-align:center;color:#fff}
.testi-name h4{font-size:24px;font-weight:700}
.testi-name span{font-size:12px}
.dots{left:575px;top:3818px;display:flex;gap:8px}
.dots i{width:8px;height:8px;border-radius:50%;background:rgba(255,255,255,.5)}
.dots i.on{background:#fff}

/* badges */
.badges{left:0;top:3852px;width:1200px;height:210px;background:var(--green)}
.badge-row{left:155px;top:3905px;width:900px;display:flex;justify-content:space-between;align-items:center}
.badge{background:rgba(255,255,255,.85)}

/* footer */
.footer{left:0;top:4062px;width:1200px;height:383px;background:var(--footer)}
.footer-bottom{left:0;top:4445px;width:1200px;height:44px;background:var(--footer-dark);color:#aaa;font-size:9px;padding:16px 235px}
.fcol h5{font-size:12px;color:#fff;font-weight:700;margin-bottom:16px}
.fcol li{list-style:none;font-size:11px;color:#ddd;line-height:18px}
.social{display:flex;gap:10px;margin-top:18px}
.social i{width:28px;height:28px;background:var(--blue);display:block}
.post{display:flex;gap:14px;margin-bottom:22px}
.post .ic{width:48px;height:48px;flex:none;display:flex;align-items:center;justify-content:center}
.post p{font-size:10px;color:#ddd;line-height:14px}
.post span{font-size:10px;color:#fff;font-weight:700}
</style>
</head>
<body>

<div class="abs topbar">
  <div><span>&#9742; 303-555-0148</span><span>&#9993; info@trypelmarix.com</span></div>
  <div>Fully Licensed. 24/7 Same Day Response</div>
</div>

<div class="abs hero">
  <div class="abs hero-photo" role="img" aria-label="Blue-toned photo of a dusty inspection site"></div>
  <svg class="abs" style="left:0;top:0" width="1200" height="870" viewBox="0 0 1200 870">
    <polygon points="0,500 640,870 0,870" fill="#fff"/>
    <polygon points="640,870 1200,540 1200,870" fill="#fff"/>
    <line x1="0" y1="580" x2="740" y2="150" stroke="#fff" stroke-opacity=".35" stroke-width="1.5"/>
    <line x1="40" y1="640" x2="780" y2="210" stroke="#fff" stroke-opacity=".35" stroke-width="1.5"/>
    <line x1="120" y1="700" x2="640" y2="400" stroke="#fff" stroke-opacity=".35" stroke-width="1.5"/>
    <line x1="200" y1="760" x2="700" y2="470" stroke="#9bcb3c" stroke-opacity=".6" stroke-width="1.5"/>
    <polygon points="620,775 632,768 644,775 644,789 632,796 620,789" fill="#0355a3"/>
    <polygon points="470,675 480,669 490,675 490,687 480,693 470,687" fill="#0355a3"/>
    <polygon points="310,600 318,595 326,600 326,610 318,615 310,610" fill="#0355a3"/>
  </svg>
  <div class="abs header">
    <div class="brand"><span class="brand-dot"></span>Trypelmarix</div>
    <nav class="nav">
      <a>Home</a><a>|</a><a>Our Services</a><a>|</a><a>Resources</a><a>|</a><a>Blog</a><a>|</a><a>Q &amp; A</a><a>|</a><a>Reviews</a><a>|</a><a>Connect</a>
    </nav>
  </div>
  <div class="abs hero-text">
    <div class="welcome">WELCOME TO <b>TRYPELMARIX</b></div>
    <h1>ASBESTOS, MOLD, LEAD<br><span class="g">INSPECTIONS</span><br><span class="g">24/7/365</span> SAME DAY SERVICE</h1>
    <p>Fast, Dependable Results When it Matters the Most. Proudly Serving Denver - Colorado Springs - Boulder</p>
    <a class="btn-white">CONTACT US</a>
  </div>
</div>

<div class="abs signup-shadow"></div>
<form class="abs signup">
  <h3>SIGNUP A NEW<br>INSPECTION</h3>
  <div class="field">NAME</div>
  <div class="field">EMAIL</div>
  <div class="field">PHONE</div>
  <div class="field tall">MESSAGE</div>
  <div style="text-align:center"><span class="btn-blue">SUBMIT</span></div>
</form>

<!-- why choose us -->
<div class="abs why-photo" role="img" aria-label="Photo of a smiling inspector in a hard hat giving a thumbs up"></div>
<div class="abs why-head"><div class="num">01</div><div class="sec-title" style="margin-bottom:6px">Why Choose Us?</div></div>

<div class="abs why-item" style="top:1070px">
  <h4><svg width="20" height="20" viewBox="0 0 20 20"><circle cx="10" cy="5" r="4" fill="#0355a3"/><rect x="5" y="10" width="10" height="10" fill="#0355a3"/></svg>WE'RE SERIOUS ABOUT OUR WORK</h4>
  <p>We'll show up at your door with a smile and treat you like a new friend. But be assured that we're all business when it comes to delivering professional testing and consulting services.</p>
</div>
<div class="abs why-item" style="top:1170px">
  <h4><svg width="20" height="20" viewBox="0 0 20 20"><circle cx="10" cy="10" r="9" fill="#0355a3"/><path d="M5 10l4 4 6-8" stroke="#fff" stroke-width="2" fill="none"/></svg>FAST, ACCURATE TEST RESULTS. VERY FAST.</h4>
  <p>For any environmental testing to be meaningful, much less valuable, you need the results to be reliable and fast. If it takes until mold spores become visible over a large area to get positive mold contamination test results, those results aren't really "news." They're "olds."</p>
</div>
<div class="abs why-item" style="top:1290px">
  <h4><svg width="20" height="20" viewBox="0 0 20 20"><path d="M1 10L10 2l9 8v9H1z" fill="#0355a3"/></svg>WE TREAT YOUR FAMILY AND BUSINESS LIKE OURS</h4>
  <p>We never forget that our business is about people. Protecting people from hazards. When we enter your home or business, we consider how we would want to protect our home or business.</p>
</div>

<!-- construction band -->
<div class="abs band"></div>
<div class="abs band-blue"></div>
<svg class="abs" style="left:290px;top:1458px" width="190" height="150" viewBox="0 0 190 150">
  <polygon points="0,0 150,0 190,75 150,150 0,150" fill="#0355a3"/>
  <polygon points="60,20 120,20 150,75 120,130 60,130 30,75" fill="#0a4a90" stroke="#fff" stroke-width="3"/>
  <circle cx="90" cy="68" r="14" fill="#fff"/>
  <rect x="72" y="52" width="36" height="8" fill="#fff"/>
  <path d="M66 108c0-14 10-20 24-20s24 6 24 20z" fill="#fff"/>
</svg>
<div class="abs band-text">
  <h2 class="band-title">New construction project?</h2>
  <p>Let us start you in the right direction with our certified asbestos inspections. Residential, commercial, schools, government properties, multi-family and more.</p>
</div>
<a class="abs btn-navy" style="left:770px;top:1560px">CALL US NOW!</a>

<!-- services -->
<div class="abs" style="left:130px;top:1660px;display:flex;align-items:flex-end;gap:6px"><div class="num">02</div><div class="sec-title" style="margin-bottom:6px">Our Services</div></div>
<p class="abs svc-intro">Asbestos, Mold, Lead Inspections Asbestos, 24/7/365 Same Day Service Fast, Dependable Results When it Matters the Most. Proudly Serving Denver - Colorado Springs - Boulder Commercial Services | Residential Services | Homeowner &amp; Contractor Services</p>

<svg class="abs" style="left:130px;top:1810px" width="940" height="270" viewBox="0 0 940 270">
  <defs>
    <linearGradient id="gA" x1="0" y1="0" x2="1" y2="1"><stop offset="0" stop-color="#8f8f8f"/><stop offset="1" stop-color="#444"/></linearGradient>
    <linearGradient id="gM" x1="0" y1="0" x2="0" y2="1"><stop offset="0" stop-color="#d7d2c8"/><stop offset="1" stop-color="#8a7e6e"/></linearGradient>
    <linearGradient id="gL" x1="0" y1="0" x2="1" y2="1"><stop offset="0" stop-color="#9aa8b8"/><stop offset="1" stop-color="#4b5f76"/></linearGradient>
  </defs>
  <g role="img" aria-label="Close-up of asbestos fibre material"><polygon points="70,0 200,0 270,130 200,260 70,260 0,130" fill="url(#gA)"/></g>
  <g role="img" aria-label="Photo of mold on a wall"><polygon points="395,0 525,0 595,130 525,260 395,260 325,130" fill="url(#gM)"/></g>
  <g role="img" aria-label="Photo of cracked lead-based paint"><polygon points="710,0 840,0 910,130 840,260 710,260 640,130" fill="url(#gL)"/></g>
  <text x="135" y="90" text-anchor="middle" font-family="Roboto,sans-serif" font-size="16" font-weight="700" fill="#fff">Asbestos Testing</text>
  <text x="135" y="112" text-anchor="middle" font-family="Roboto,sans-serif" font-size="10" fill="#fff">Lorem ipsum dolor sit amet,</text>
  <text x="135" y="126" text-anchor="middle" font-family="Roboto,sans-serif" font-size="10" fill="#fff">consectetur adipiscing elit,</text>
  <text x="135" y="140" text-anchor="middle" font-family="Roboto,sans-serif" font-size="10" fill="#fff">sed do eiusmod tempor incididunt</text>
  <text x="135" y="154" text-anchor="middle" font-family="Roboto,sans-serif" font-size="10" fill="#fff">ut labore et dolore magna.</text>
</svg>
<div class="abs svc-label" style="left:115px;top:2082px">Asbestos Testing</div>
<div class="abs svc-label" style="left:455px;top:2082px">Mold Testing</div>
<div class="abs svc-label" style="left:765px;top:2082px">Lead Based Paint<br>Testing</div>

<!-- about -->
<div class="abs about"></div>
<div class="abs" style="left:215px;top:2225px;display:flex;align-items:flex-end;gap:6px"><div class="num">03</div><div class="sec-title" style="margin-bottom:6px">About Us</div></div>
<div class="abs about-photo" role="img" aria-label="Portrait photo of the owner in a suit"></div>
<div class="abs about-name"><h4>Dale Weston</h4><span>Owner</span></div>
<p class="abs about-bio">In his experience with inspecting property and mitigating environmental issues, Dale saw one project after another brought to a standstill awaiting testing results. He believed property owners should be able to get test results in hours, not days. Trypelmarix was born.</p>
<div class="abs about-copy">
  <h3>Environmental Testing Evolved</h3>
  <p>Trypelmarix grew up in the tough and tumble disaster restoration industry. Time and time again, we saw projects small and large brought to a stand-still to await environmental testing and results.</p>
  <p>First, we had to know when it's prudent or even required by law to test for asbestos, lead-based paint, mold or other contaminants. Then we had to track down reliable testing companies, facilities or equipment. Next, we had to ensure we safeguarded people and property in the process of obtaining test samples.</p>
  <p>Finally, we had to wait, sometimes days or even weeks, while property owners languished and spent more and more money on expensive temporary living or working space. We just knew there had to be a better way.</p>
  <h3 style="margin-top:14px">The Next Step</h3>
  <p>At Trypelmarix, we are experienced in assessing the environmental hazards that merit or even require testing by law. We are trained and certified to safely obtain environmental test samples.</p>
  <p>And we have established a working relationship with top-rated testing facilities that enable us to get most test results within hours, not days.</p>
</div>

<!-- call band -->
<div class="abs callband"></div>
<div class="abs callbtn">
  <svg width="22" height="22" viewBox="0 0 24 24"><path d="M6.6 10.8a15 15 0 006.6 6.6l2.2-2.2a1 1 0 011-.25 11.4 11.4 0 003.6.57 1 1 0 011 1V20a1 1 0 01-1 1A17 17 0 013 4a1 1 0 011-1h3.5a1 1 0 011 1c0 1.25.2 2.45.57 3.57a1 1 0 01-.25 1z" fill="#fff"/></svg>
  CALL US NOW 303-555-0148
</div>

<!-- blog -->
<div class="abs blog-blue">
  <div class="num" style="font-size:70px;line-height:66px">04</div>
  <h3>Blog Update</h3>
  <p>In his experience with inspecting property and mitigating environmental issues, Dale saw one project after another brought to a standstill awaiting testing.</p>
  <div style="margin-top:40px;text-align:center;font-size:30px;font-weight:300">&larr; / &rarr;</div>
</div>
<div class="abs card" style="left:464px;top:2996px;width:278px;height:335px">
  <div role="img" aria-label="Photo of peeling paint on a wall" style="height:168px;background:linear-gradient(135deg,#c9dcd6,#8fb0a8)"></div>
  <div style="padding:18px 22px">
    <div class="meta">Lorem ipsum dolor</div>
    <h4 style="margin-top:12px">Lorem ipsum dolor sit amet, consectetur</h4>
  </div>
</div>
<div class="abs card" style="left:775px;top:2985px;width:272px;height:355px;padding:22px">
  <div class="meta">Lorem ipsum dolor</div>
  <h4 style="margin:12px 0 14px">Lorem ipsum dolor sit amet, consectetur</h4>
  <p>In his experience with inspecting property and mitigating environmental issues, Dale saw one project after another brought to a standstill awaiting testing results.</p>
  <p style="margin-top:12px">Results. He believed property owners should be able to get test results in hours, not days. Trypelmarix was born.</p>
  <div style="display:flex;justify-content:space-between;margin-top:40px;font-size:10px;color:#444">
    <span>&#128197; May 4th, 2017</span><span>&#128172; 2 Comments</span>
  </div>
</div>

<!-- testimonial -->
<div class="abs testi" role="img" aria-label="Blue-toned background photo of an inspection site"></div>
<div class="abs testi-avatar" role="img" aria-label="Portrait of the reviewer"></div>
<svg class="abs" style="left:540px;top:3545px" width="34" height="34" viewBox="0 0 34 34"><circle cx="17" cy="17" r="17" fill="#0355a3"/><text x="17" y="27" text-anchor="middle" font-family="Roboto,sans-serif" font-size="24" font-weight="900" fill="#fff">&#8220;</text></svg>
<p class="abs testi-quote">In his experience with inspecting property and mitigating environmental issues, Dale saw one project after another brought to a standstill awaiting testing results. He believed property owners should be able to get test results in hours, not days. Trypelmarix was born.</p>
<div class="abs testi-name"><h4>Owen Pratt</h4><span>Home Owner</span></div>
<div class="abs dots"><i></i><i class="on"></i><i></i><i></i></div>

<!-- badges -->
<div class="abs badges"></div>
<div class="abs badge-row">
  <div class="badge" style="width:150px;height:70px;border-radius:6px"></div>
  <div class="badge" style="width:150px;height:70px;border-radius:6px"></div>
  <div class="badge" style="width:110px;height:110px;border-radius:50%"></div>
  <div class="badge" style="width:210px;height:80px;border-radius:6px"></div>
  <div class="badge" style="width:150px;height:70px;border-radius:6px"></div>
</div>

<!-- footer -->
<div class="abs footer"></div>
<div class="abs fcol" style="left:235px;top:4160px;width:210px">
  <div class="brand" style="color:#fff;font-size:24px;margin-bottom:14px"><span class="brand-dot"></span>Trypelmarix</div>
  <p style="font-size:10px;line-height:14px;color:#ccc">Lorem ipsum dolor sit amet, consectetur adipiscing elit, sed do eiusmod tempor incididunt ut labore et dolore magna aliqua. Ut enim ad minim veniam, quis nostrud exercitation ullamco.</p>
  <div class="social"><i></i><i></i><i></i><i></i><i></i></div>
</div>
<div class="abs fcol" style="left:530px;top:4160px">
  <h5>QUICK LINKS</h5>
  <ul><li>HOME</li><li>OUR SERVICES</li><li>RESOURCES</li><li>BLOG</li><li>Q &amp; A</li><li>REVIEWS</li><li>CONNECT</li></ul>
</div>
<div class="abs fcol" style="left:738px;top:4160px;width:260px">
  <h5>RECENT POSTS</h5>
  <div class="post"><div class="ic" style="background:var(--blue)"><svg width="18" height="18" viewBox="0 0 18 18"><path d="M2 16l1-4 9-9 3 3-9 9z" fill="#fff"/></svg></div><div><p>LOREM IPSUM DOLOR SIT AMET, CONSECTETUR ADIP.</p><span>29 JUNE 2017</span></div></div>
  <div class="post"><div class="ic" style="background:var(--green)"><svg width="18" height="18" viewBox="0 0 18 18"><path d="M2 16l1-4 9-9 3 3-9 9z" fill="#fff"/></svg></div><div><p>LOREM IPSUM DOLOR SIT AMET, CONSECTETUR ADIP.</p><span>31 JUNE 2017</span></div></div>
</div>
<div class="abs footer-bottom">© COPYRIGHT TRYPELMARIX. ALL RIGHTS RESERVED</div>

</body>
</html>
```